FlockVault.net website design

We are looking for a design for a new website we are about to launch called FlockVault.net. FlockVault.net is an online discount wine site that will focus on selling only one wine at a time. (This potentially may become two or three wines at a time in the future but only one for now). The wine that is up for sale will not actually be sold until a pre-set number of buyers “the group” commits to buying the wine. If the threshold of buyers is not met then the wine is not sold. This group aspect is what makes the site unique. By only selling the wine when the group commits to buying it we are able to deliver them a great wine at a fantastic price.
The website should convey a fun feeling while also indicating that this is a place where serious wine enthusiasts can shop. We will be providing information, ratings, and reviews about the wines that are currently on sale.
Updates
Target Market(s)
The target market is a wide range of wine enthusiasts, from people in their 20s and 30s to more mature and serious wine connoisseurs.
Industry/Entity Type
Shop
Requirements
Must have
- Below is a list of specifications for the website:
1) Main page with our logo (which includes green, purple, and a magenta wine color) that showcases the current wine that's for sale
- The site’s main focus should be on selling ONE bottle of wine at a time at group rate.
- The site should capture the group buying concept as this is what differentiates our site from the others. Visitors to the site should get the sense that they are part of a special community that is getting a great deal because they are buying the wine as a group.
- A meter or better yet an animation should be used to indicate if the tipping point has been met for a sale. We’d like to see some creative ideas here.
- Nice high-res photo of the wine bottle
- Detailed description of what kind of wine it is, where the wine is from, type of grape, vino observer and other ratings, description of what it tastes like. We would like the option to provide as much detail here as possible.
- Breakdown on what the prices are per bottle and the discount we're giving. We would like to show the original price as compared to the FlockVault.net price.
- Potentially show a list of upcoming wines. Maybe not the exact wine that will be for sale next but some info to entice users to keep checking.
2) User Account Log in
- Ability to create and log into a personal account
The personal account should be able to:
-store users' credit card and shipping information as well as past orders
-allow you to opt in or out of flock vault emails
-potentially store wine preference or ratings information
-refer a friend option where you get some kind of incentive
3) The Group Concept. The website design must include a few aspects that identify FlockVault.net as a social site, not simply a wine sale site.
- Some kind of indicator showing if the group threshold has been met or not. We would like to see some type of animation with wine bottles filling up, or grapes on a scale-something that would change as the number of people buying into the sale increase.
- Button to join the group purchase
4) General Site Content must include:
- Email link to send questions to support
- Information on how shipping works and other FAQs
- Legal disclaimer
- Links to Facebook and Twitter
Nice to have
- It would be nice to have a discussion board where FlockVault members can discuss wines.
Should not have
- The design should not be for a general wine store that sells a variety of different wines.

```html
<!DOCTYPE html>
<html lang="en">
<head>
<meta charset="utf-8">
<title>FlockVault.net — How it works</title>
<link rel="stylesheet" href="https://fonts.googleapis.com/css2?family=Lobster&family=Merriweather:wght@400&family=Lobster+Two:ital@1&family=Cabin:wght@400&display=swap">
<style>
  :root {
    --cream: #fbf5ea;
    --tab: #f2f3f7;
    --tab-edge: #b9b9c8;
    --ink: #4a4448;
    --green: #8cc63f;
    --magenta: #b5306e;
    --wood: #a5460e;
    --wood-dark: #8a3707;
    --wood-light: #b2520f;
    --grain-dark: rgba(70, 20, 0, 0.10);
    --grain-light: rgba(255, 170, 90, 0.06);
    --text-light: #fdf3ea;
    --btn-top: #f0a04f;
    --btn-bottom: #d4772a;
    --btn-ink: #4a1c08;
  }
  * { box-sizing: border-box; margin: 0; padding: 0; }
  html, body { width: 1200px; height: 900px; overflow: hidden; }
  body {
    position: relative;
    background: var(--wood);
    font-family: "Merriweather", Georgia, serif;
  }
  .topbar {
    position: absolute; left: 0; top: 0; width: 1200px; height: 84px;
    background: var(--cream);
    border-bottom: 2px solid #7a3208;
  }
  .topbar::before {
    content: ""; position: absolute; left: 0; top: 0; width: 100%; height: 12px;
    background:
      repeating-linear-gradient(90deg, rgba(150,60,90,0.25) 0 2px, transparent 2px 5px),
      linear-gradient(#c98a94, #e9c9c4);
  }
  .tab {
    position: absolute; top: 12px; height: 70px;
    background: var(--tab);
    border-left: 1px dotted var(--tab-edge);
    border-right: 1px dotted var(--tab-edge);
  }
  .tab-icon { position: absolute; left: 8px; top: 10px; }
  .tab-title {
    position: absolute; left: 40px; top: 9px;
    font-family: "Cabin", sans-serif; font-size: 22px; color: var(--ink);
    white-space: nowrap;
  }
  .tab-sub {
    position: absolute; top: 33px; right: 42px;
    font-family: "Lobster Two", cursive; font-style: italic; font-size: 17px;
  }
  .tab-how { left: 135px; width: 220px; }
  .tab-how .tab-sub { color: var(--green); }
  .tab-latest { left: 632px; width: 197px; }
  .tab-latest .tab-sub { color: var(--magenta); right: 24px; }

  .panel {
    position: absolute;
    background:
      repeating-linear-gradient(0deg, var(--grain-dark) 0 1px, transparent 1px 3px, var(--grain-light) 3px 4px, transparent 4px 7px),
      repeating-linear-gradient(0deg, rgba(60,15,0,0.07) 0 2px, transparent 2px 11px, rgba(255,150,70,0.05) 11px 13px, transparent 13px 23px),
      repeating-linear-gradient(90deg, rgba(60,15,0,0.04) 0 1px, transparent 1px 37px, rgba(255,160,80,0.04) 37px 39px, transparent 39px 83px),
      repeating-linear-gradient(2deg, transparent 0 17px, rgba(80,25,0,0.05) 17px 18px, transparent 18px 41px),
      linear-gradient(180deg, var(--wood-light), var(--wood) 25%, var(--wood) 80%, var(--wood-dark));
  }
  .row-divider { position: absolute; left: 0; width: 1200px; height: 8px;
    background: linear-gradient(rgba(90,32,3,0.9), rgba(110,44,5,0)); }
  .col-divider { position: absolute; left: 631px; width: 1px; background: rgba(90,30,0,0.45); }
  .soft-rule { position: absolute; left: 0; top: 421px; width: 631px; height: 1px; background: rgba(90,30,0,0.3); }

  .heading {
    position: absolute; font-family: "Lobster", cursive; font-size: 26.5px; font-weight: 400;
    color: #fff; text-shadow: 0 1px 2px rgba(0,0,0,0.35); white-space: nowrap;
  }
  .body-copy {
    font-size: 12.6px; line-height: 17.9px; letter-spacing: 0.35px;
    color: var(--text-light); hyphens: auto; -webkit-hyphens: auto;
  }
  .story { position: absolute; left: 135px; width: 467px; }
  .story .photo { float: left; width: 122px; height: 115px; margin: 3px 17px 2px 0; }
  .photo { border: 2px solid #fff; box-shadow: 2px 3px 5px rgba(0,0,0,0.45); }
  .photo-bottles { background: radial-gradient(circle at 40% 35%, #d9a441, #6b3a10 55%, #1c0d05); }
  .photo-pour { background: radial-gradient(circle at 60% 55%, #b01a2a, #e9d6d6 45%, #fff 70%); }
  .photo-barrel { background: radial-gradient(circle at 65% 30%, #8c5a2c, #3b2010 50%, #0c0604); }

  .btn {
    position: absolute; height: 28px;
    background: linear-gradient(var(--btn-top), var(--btn-bottom));
    border-radius: 3px; box-shadow: 1px 2px 4px rgba(0,0,0,0.45);
    font-family: "Lobster Two", cursive; font-style: italic; font-size: 16px;
    color: var(--btn-ink); text-align: center; line-height: 27px;
  }
  .btn-join { width: 106px; }
  .btn-view { width: 67px; }

  .quote { position: absolute; left: 148px; top: 455px; width: 424px; }

  .wine-item { position: absolute; left: 662px; width: 440px; height: 100px; }
  .wine-item .photo { position: absolute; left: 0; top: 0; width: 81px; height: 72px; }
  .wine-item p { position: absolute; left: 100px; top: 6px; width: 336px; }
  .wine-item .btn { left: 325px; top: 60px; }
</style>
</head>
<body>
  <header class="topbar">
    <div class="tab tab-how">
      <svg class="tab-icon" width="26" height="26" viewBox="0 0 26 26"><circle cx="13" cy="13" r="11" fill="var(--magenta)"/></svg>
      <span class="tab-title">how it works?</span>
      <span class="tab-sub">join the cellar!</span>
    </div>
    <div class="tab tab-latest">
      <svg class="tab-icon" width="26" height="26" viewBox="0 0 26 26"><circle cx="13" cy="13" r="11" fill="var(--magenta)"/></svg>
      <span class="tab-title">latest wines</span>
      <span class="tab-sub">you've tasted</span>
    </div>
  </header>

  <div class="panel" style="left:0;top:86px;width:1200px;height:490px"></div>
  <div class="panel" style="left:0;top:576px;width:1200px;height:324px"></div>
  <div class="row-divider" style="top:574px"></div>
  <div class="col-divider" style="top:84px;height:816px"></div>
  <div class="soft-rule"></div>

  <h2 class="heading" style="left:200px;top:106px">Community buying is cheaper</h2>
  <div class="story body-copy" style="top:171px">
    <div class="photo photo-bottles" role="img" aria-label="Wine bottles, glasses and grapes"></div>
    Quisque auctor velit ut est mollis sed bibendum magna congue. Aenean vulputate risus mattis lectus vulputate iaculis. Duis sit amet sapien in felis fringilla viverra. Nullam tortor nulla, tristique id mollis fringilla, imperdiet id ipsum. Fusce id tellus ligula. Phasellus non felis nec magna aliquam adipiscing id in magna. Maece&shy;sodales massa faucibus tempor non quis mauris. Integer aliquam mauris urna, et fringilla lorem.
  </div>
  <div class="btn btn-join" style="left:426px;top:346px">join now</div>

  <p class="quote body-copy">“Proin vitae hendrerit justo. In ullamcorper, augue ullamcor&shy;per consectetur convallis, purus odio vulputate diam, a pulvi&shy;nar leo mauris nec ante. ”</p>
  <div class="btn btn-view" style="left:462px;top:504px">view</div>

  <h2 class="heading" style="left:702px;top:106px">Duis sit amet sapien</h2>
  <div class="wine-item" style="top:174px">
    <div class="photo photo-barrel" role="img" aria-label="Wine bottle and glass before a barrel"></div>
    <p class="body-copy">Duis sit amet sapien in felis fringilla viverra. Nullam tortor nulla, tristique id mollis fringilla, imperdiet id ipsum.</p>
    <div class="btn btn-view">view</div>
  </div>
  <div class="wine-item" style="top:294px">
    <div class="photo photo-barrel" role="img" aria-label="Wine bottle and glass before a barrel"></div>
    <p class="body-copy">Duis sit amet sapien in felis fringilla viverra. Nullam tortor nulla, tristique id mollis fringilla, imperdiet id ipsum.</p>
    <div class="btn btn-view">view</div>
  </div>
  <div class="wine-item" style="top:404px">
    <div class="photo photo-barrel" role="img" aria-label="Wine bottle and glass before a barrel"></div>
    <p class="body-copy">Duis sit amet sapien in felis fringilla viverra. Nullam tortor nulla, tristique id mollis fringilla, imperdiet id ipsum.</p>
    <div class="btn btn-view">view</div>
  </div>

  <h2 class="heading" style="left:200px;top:613px">Non quis integer aliquam</h2>
  <div class="story body-copy" style="top:678px">
    <div class="photo photo-pour" role="img" aria-label="Red wine splashing into a glass"></div>
    Quisque auctor velit ut est mollis sed bibendum magna congue. Aenean vulputate risus mattis lectus vulputate iaculis. Duis sit amet sapien in felis fringilla viverra. Nullam tortor nulla, tristique id mollis fringilla, imperdiet id ipsum. Fusce id tellus ligula. Phasellus non felis nec magna aliquam adipiscing id in magna. Maece&shy;sodales massa faucibus tempor non quis mauris. Integer aliquam mauris urna, et fringilla lorem.
  </div>
  <div class="btn btn-join" style="left:426px;top:853px">join now</div>

  <h2 class="heading" style="left:702px;top:613px">Duis sit amet sapien</h2>
  <div class="wine-item" style="top:681px">
    <div class="photo photo-barrel" role="img" aria-label="Wine bottle and glass before a barrel"></div>
    <p class="body-copy">Duis sit amet sapien in felis fringilla viverra. Nullam tortor nulla, tristique id mollis fringilla, imperdiet id ipsum.</p>
    <div class="btn btn-view">view</div>
  </div>
  <div class="wine-item" style="top:801px">
    <div class="photo photo-barrel" role="img" aria-label="Wine bottle and glass before a barrel"></div>
    <p class="body-copy">Duis sit amet sapien in felis fringilla viverra. Nullam tortor nulla, tristique id mollis fringilla, imperdiet id ipsum.</p>
    <div class="btn btn-view">view</div>
  </div>
</body>
</html>
```